Catchy Cards for Hospital

I run a rural hospital in Texas called Pellor Valley Hospital and am in need of contemporary business cards for all of my Department Heads. While our logo is somewhat simplistic, I don't have the option of changing it at this time, so anything to make the rest of the card present the appearance of a modern, professional healthcare facility would be great. Although the attached files are in black, our hospital colors are in a copper brown and black. I need to be able to change the name and title on the card so I can get cards printed for various department heads.

Target Market(s)

Referring physicians, large hospital systems, national organizations, state and federal government

Industry/Entity Type

Hospital

Contact Information for Business Card

Name Dale Hoskin
Title CEO

Phone: Main 325-555-0147 & Direct xxxxxx
Fax xxxxx
dale.hoskin@pellorvh.example
382 Wimble Street Box 415
Halden Springs, Westmark 76902

Font styles to use
Serif

Colors
f48340

Requirements
Must have
• Clean crisp lines and ability to modify names, titles and emails
• On the back "PellorValleyHospital.Example
Nice to have
• Needs to be in line with logo, which is a bit dated and not too appealing, but I'm hoping that the rest of the card can make up for that fact just a little bit.
• Hospital's colors are a copper brown, black and white
Should not have
• Shapes or anything distracting

```html
<!DOCTYPE html>
<html lang="en">
<head>
<meta charset="utf-8">
<title>Pellor Valley Hospital – Business Card</title>
<link rel="stylesheet" href="https://fonts.googleapis.com/css2?family=Noto+Serif:wght@400;700&display=swap">
<style>
  :root {
    --page-bg: #ececec;
    --peach: #f6c7a6;
    --copper: #f48340;
    --copper-text: #e5772f;
    --ink: #1d1d1d;
    --photo-light: #eef0f2;
    --photo-mid: #d9dde2;
    --photo-warm: #f3e4d8;
    --photo-warm-mid: #e7d6c9;
  }
  * { margin: 0; padding: 0; box-sizing: border-box; }
  html, body { width: 1200px; height: 533px; overflow: hidden; }
  body {
    background: var(--page-bg);
    font-family: "Noto Serif", Georgia, serif;
    position: relative;
  }
  .card {
    position: absolute;
    top: 89px;
    width: 540px;
    height: 307px;
    overflow: hidden;
    box-shadow: 0 2px 6px rgba(0,0,0,0.12);
  }
  .card--front { left: 60px; }
  .card--back { left: 627px; }

  .photo { position: absolute; top: 0; bottom: 0; }
  .card--front .photo {
    left: 250px; right: 0;
    background: linear-gradient(135deg, var(--photo-light) 0%, var(--photo-mid) 55%, #c9ced6 100%);
  }
  .card--back .photo {
    left: 53px; right: 0;
    background: linear-gradient(135deg, var(--photo-warm) 0%, var(--photo-warm-mid) 60%, #dccbbd 100%);
  }
  .shape-layer { position: absolute; inset: 0; }

  .front-text { position: absolute; inset: 0; color: var(--copper-text); }
  .holder-name {
    position: absolute; left: 40px; top: 30px;
    font-size: 17px; font-weight: 700;
  }
  .holder-title { position: absolute; left: 40px; top: 55px; font-size: 12px; }
  .contact-list {
    position: absolute; left: 40px; top: 124px;
    font-size: 9.5px; line-height: 13px;
  }
  .contact-row { display: flex; margin-bottom: 14px; }
  .contact-label { width: 42px; font-weight: 700; }
  .contact-value { display: block; }

  .hospital-name {
    position: absolute;
    left: 330px; top: 140px;
    width: 170px;
    font-size: 17px; font-weight: 700;
    line-height: 20px;
    color: var(--ink);
  }

  .back-strip {
    position: absolute; left: 0; top: 0; bottom: 0; width: 36px;
    background: var(--peach);
  }
  .back-band {
    position: absolute; left: 36px; top: 0; bottom: 0; width: 17px;
    background: var(--copper);
  }
  .web-address {
    position: absolute;
    left: 18px; top: 150px;
    transform: translate(-50%, -50%) rotate(-90deg);
    white-space: nowrap;
    font-size: 10px;
    color: var(--copper-text);
  }
</style>
</head>
<body>

  <section class="card card--front" aria-label="Business card front">
    <div class="photo" role="img" aria-label="Photo of a stethoscope resting on a smartphone on a white desk"></div>
    <svg class="shape-layer" viewBox="0 0 540 307" preserveAspectRatio="none" aria-hidden="true">
      <path d="M0 0 H268 C262 90 258 200 265 307 H0 Z" fill="var(--peach)"/>
      <path d="M268 0 C262 90 258 200 265 307" fill="none" stroke="var(--copper)" stroke-width="3"/>
    </svg>
    <div class="front-text">
      <p class="holder-name">Dale Hoskin</p>
      <p class="holder-title">CEO</p>
      <div class="contact-list">
        <div class="contact-row"><span class="contact-label">Phone</span><span><span class="contact-value">325-555-0147</span><span class="contact-value">325-555-0147</span></span></div>
        <div class="contact-row"><span class="contact-label">Fax</span><span class="contact-value">325-555-0183</span></div>
        <div class="contact-row"><span class="contact-label">E-mail</span><span class="contact-value">dale.hoskin@pellorvh.example</span></div>
        <div class="contact-row"><span class="contact-label">Address</span><span><span class="contact-value">382 Wimble Street Box 415</span><span class="contact-value">Halden Springs, Westmark 76902</span></span></div>
      </div>
    </div>
    <p class="hospital-name">Pellor Valley Hospital</p>
  </section>

  <section class="card card--back" aria-label="Business card back">
    <div class="photo" role="img" aria-label="Faded photo of a stethoscope resting on a smartphone"></div>
    <svg class="shape-layer" viewBox="0 0 540 307" preserveAspectRatio="none" aria-hidden="true">
      <path d="M428 0 C412 90 410 210 424 307 H540 V0 Z" fill="var(--copper)"/>
    </svg>
    <div class="back-strip"></div>
    <div class="back-band"></div>
    <p class="web-address">PellorValleyHospital.Example</p>
  </section>

</body>
</html>
```